Postcard design for accounting company

We need a postcard design (front and back) to our accounting firm that provides bookkeeping services to small and mid-size companies using LedgerPad Online. We would like to see designs that use the color blue and match our overall branding (see website). The final design should communicate professionalism, trust, and ease.

Target Market(s)

Small and Mid-Size companies

Industry/Entity Type

Accounting

Colors
0054AA
0677BA
7BADD7
CADEEF
E8F1F8

Requirements
Must have
• Logo, contact information, indicate services offered, color blue, and fit postcard template (see attached). Contact info = 555.318.2207, 1.800.555.0142, Info@BrightLedgerAccounting.com, www.BrightLedgerAccounting.com. Use the ZRPX Retail Indicia, which is a postage payment mark that takes the place of a regular postage stamp or meter stamp. Every ZRPX mailpiece must include the ZRPX Retail Indicia above and to the right of the address block. The ZRPX Retail Indicia does not have a specific size requirement but must be larger than 0.5" x 0.5". The type font must be in all caps and at least a 4 point size. It should fit in the area 1.625" from the right edge and 1.375" from top edge. Leave 1/8" of space around the top and right edge. See attached sample.
Nice to have
• Include that we a re Certified LedgerPad CertPartners (can include LPO logo). Also, maybe include the logos of the associations we are members of (North Pinecrest Chamber of Commerce, Federal Guild of Certified Ledgerkeepers, and Continental League of Female Enterprise Founders.

```html
<!DOCTYPE html>
<html lang="en">
<head>
<meta charset="utf-8">
<title>Bright Ledger Accounting – Postcard</title>
<link rel="stylesheet" href="https://fonts.googleapis.com/css2?family=Montserrat:wght@400;500;600;700;800&display=swap">
<style>
:root{
  --navy:#0a1f4d;
  --deep:#0054AA;
  --mid:#0677BA;
  --sky:#7BADD7;
  --pale:#CADEEF;
  --ice:#E8F1F8;
  --green:#5cc43c;
  --ink:#1b2a44;
}
*{margin:0;padding:0;box-sizing:border-box}
html,body{width:1200px;height:2602px;overflow:hidden}
body{background:linear-gradient(180deg,#bdbdbd 0%,#d4d4d4 60%,#e6e6e6 100%);font-family:"Montserrat",Arial,sans-serif;position:relative}
.card{position:absolute;left:138px;width:935px;height:630px;overflow:hidden;box-shadow:0 14px 18px rgba(0,0,0,.35)}
.front{top:1015px;background:var(--navy)}
.back{top:1768px;background:#fff}
.abs{position:absolute}

/* front */
.front-art{left:0;top:0;width:935px;height:630px}
.laptop-screen{left:512px;top:232px;width:380px;height:250px;background:linear-gradient(180deg,#f4f6f9,#dfe4ec);border:10px solid #1d2430;border-radius:8px}
.headline{left:42px;top:42px;color:#fff;font-weight:800;font-size:33px;line-height:42px;letter-spacing:.5px}
.tagline{left:40px;top:128px;color:#fff;font-size:19px;line-height:23px;font-weight:400}
.tagline b{font-weight:700}
.pill{left:40px;top:206px;height:24px;width:357px;background:var(--green);border-radius:12px;color:#fff;font-size:14px;font-weight:600;display:flex;align-items:center;gap:8px;padding-left:4px}
.pill .dot{width:20px;height:20px;border:2px solid #fff;border-radius:50%}
.pk-title{left:37px;top:254px;color:#fff;font-size:27px;font-weight:400}
.pk-title b{font-weight:700}
.services-tab{left:0;top:290px;width:28px;height:95px;background:var(--deep);border-radius:0 6px 6px 0;color:#fff;font-size:13px;font-weight:600;display:flex;align-items:center;justify-content:center}
.services-tab span{transform:rotate(-90deg);white-space:nowrap}
.pk-list{list-style:none;color:#fff;font-size:14px;line-height:17.8px;font-weight:500}
.pk-list li{display:flex;align-items:center;gap:11px}
.pk-list li::before{content:"";width:9px;height:9px;border-radius:50%;background:#fff;flex:none}
.contacts{color:#fff;font-size:13px;font-weight:500;line-height:23.5px}
.contacts .row{display:flex;align-items:center;gap:6px}
.contacts .ico{width:17px;height:17px;border:1.5px solid currentColor;border-radius:50%;display:inline-block;flex:none}
.contacts .sep{margin:0 4px}
.contacts .hl{color:var(--sky)}
.brand{left:768px;top:48px;display:flex;align-items:center;gap:7px;color:var(--deep);font-size:17px;font-weight:700;line-height:19px}
.brand .sq{width:14px;height:14px;background:var(--deep);flex:none}

/* back */
.back-panel{left:0;top:0;width:560px;height:500px}
.sec{left:42px;color:#fff}
.sec h2{font-size:22px;font-weight:800;display:flex;align-items:center;gap:9px;letter-spacing:.3px}
.sec h2::before{content:"";width:16px;height:16px;border-radius:50%;background:#fff;flex:none}
.sec p{font-size:14.2px;line-height:19px;font-weight:500;margin-top:4px}
.back .contacts{color:var(--ink);font-size:15px;line-height:30px}
.back .contacts .hl{color:var(--deep)}
.badges{left:558px;top:70px;display:flex;gap:12px;align-items:center}
.badge{width:46px;height:46px;border-radius:50%;border:3px solid #d9c27a;background:#f3efe0}
.badge.green{border-color:#2c8a3c;background:#eef6ee}
.badge.teal{border-color:#167f7a;background:#eef5f5}
.badge.shield{border-radius:6px;border-color:#5cc43c;background:#f2faef}
.indicia{left:786px;top:35px;width:112px;height:112px;border:1.5px solid #222;display:flex;align-items:center;justify-content:center;text-align:center;font-size:13.5px;line-height:19px;font-weight:500;color:#111}
.brand-faint{left:518px;top:478px;color:var(--ice);font-size:42px;font-weight:700;line-height:48px}
</style>
</head>
<body>

<section class="card front" aria-label="Postcard front">
  <svg class="abs front-art" viewBox="0 0 935 630" aria-hidden="true">
    <defs>
      <linearGradient id="city-fill" x1="0" y1="0" x2="1" y2="1">
        <stop offset="0" stop-color="#0b2a66"/>
        <stop offset=".45" stop-color="#123e86"/>
        <stop offset="1" stop-color="#08183a"/>
      </linearGradient>
      <linearGradient id="desk-fill" x1="0" y1="0" x2="0" y2="1">
        <stop offset="0" stop-color="#e9eef6"/>
        <stop offset=".55" stop-color="#d7dfeb"/>
        <stop offset="1" stop-color="#aeb9c9"/>
      </linearGradient>
      <linearGradient id="base-shade" x1="0" y1="0" x2="1" y2="0">
        <stop offset="0" stop-color="#03060d"/>
        <stop offset=".45" stop-color="#03060d" stop-opacity=".85"/>
        <stop offset=".8" stop-color="#03060d" stop-opacity="0"/>
      </linearGradient>
      <linearGradient id="swoosh-fill" x1="0" y1="1" x2="1" y2="0">
        <stop offset="0" stop-color="#0b3f96"/>
        <stop offset="1" stop-color="#1f7fd6"/>
      </linearGradient>
    </defs>
    <rect width="935" height="630" fill="url(#city-fill)" role="img" aria-label="Night city skyline in deep blue tones"/>
    <path d="M752 0 L935 0 L935 630 L0 630 L0 535 C280 490 520 400 745 250 Z" fill="url(#desk-fill)" role="img" aria-label="Laptop on a bright white office desk"/>
    <rect x="0" y="540" width="760" height="90" fill="url(#base-shade)"/>
    <path d="M0 505 C250 450 430 360 560 255 L515 240 L747 0 L752 0 L745 250 C520 400 280 490 0 535 Z" fill="url(#swoosh-fill)"/>
    <path d="M0 541 C280 496 520 406 748 256" fill="none" stroke="#fff" stroke-width="6"/>
  </svg>

  <div class="abs laptop-screen" role="img" aria-label="Accounting dashboard on the laptop screen"></div>

  <div class="abs brand"><span class="sq"></span><span>Bright Ledger<br>Accounting</span></div>

  <h1 class="abs headline">ACCOUNTING<br>FOR YOUR BUSINESS</h1>
  <p class="abs tagline"><b>Specializing</b> in Cloud-Based<br>Bookkeeping &amp; Payroll Processing with<br>LedgerPad Online by Quillstone.</p>
  <div class="abs pill"><span class="dot"></span>We a re Certified LedgerPad CertPartners</div>

  <h2 class="abs pk-title">BOOKKEEPING <b>PACKAGES</b></h2>
  <div class="abs services-tab"><span>SERVICES</span></div>
  <ul class="abs pk-list" style="left:42px;top:296px">
    <li>Accounts Receivable</li>
    <li>Accounts Payable</li>
    <li>Inventory</li>
    <li>Payroll</li>
    <li>Accruals/Adjusting Entries</li>
  </ul>
  <ul class="abs pk-list" style="left:268px;top:296px">
    <li>Account Reconciliation</li>
    <li>Financial Reporting</li>
    <li>Sales Tax</li>
    <li>Consulting</li>
  </ul>

  <div class="abs contacts" style="left:40px;top:536px">
    <div class="row"><span class="ico"></span><span>555.318.2207</span><span class="sep">|</span><span class="ico"></span><span>1.800.555.0142</span></div>
    <div class="row"><span class="ico"></span><span>Info@<span class="hl">BrightLedgerAccounting</span>.com</span></div>
    <div class="row"><span class="ico"></span><span>www.<span class="hl">BrightLedgerAccounting</span>.com</span></div>
  </div>
</section>

<section class="card back" aria-label="Postcard back">
  <svg class="abs back-panel" viewBox="0 0 560 500" role="img" aria-label="Blue-toned photo of a business team at work">
    <defs>
      <linearGradient id="panel-fill" x1="0" y1="0" x2="1" y2="1">
        <stop offset="0" stop-color="#0054AA"/>
        <stop offset=".6" stop-color="#0a5fc0"/>
        <stop offset="1" stop-color="#0677BA"/>
      </linearGradient>
    </defs>
    <polygon points="0,0 457,0 547,155 347,500 0,500" fill="url(#panel-fill)"/>
  </svg>

  <div class="abs sec" style="top:30px">
    <h2>BOOKKEEPING</h2>
    <p>Let us take over the day to day bookkeeping so you<br>can get back to running your business. We offer<br>LedgerPad Online setup and ongoing bookkeeping,<br>including daily journal entries, accounts payables &amp;<br>receivables, bill pay, sales tax reporting &amp; payments,<br>account reconciliation, and more.</p>
  </div>
  <div class="abs sec" style="top:192px">
    <h2>FINANCIAL REPORTING</h2>
    <p>We'll provide easy to understand financial reports that<br>allow you and your team to manage cash flow, create<br>budgets and make forecasting decisions. &nbsp;Want real<br>time data? &nbsp;Let us provide solutions with the latest in<br>mobile apps and dashboards.</p>
  </div>
  <div class="abs sec" style="top:336px">
    <h2>PAYROLL PROCESSING</h2>
    <p>We'll provide easy to understand financial<br>reports that allow you and your team to<br>manage cash flow, create budgets and make<br>forecasting decisions. &nbsp;Want real time data?<br>Let us provide solutions with the latest in<br>mobile apps and dashboards.</p>
  </div>

  <div class="abs badges" aria-label="Member associations">
    <span class="badge green" role="img" aria-label="North Pinecrest Chamber of Commerce badge"></span>
    <span class="badge" role="img" aria-label="Federal Guild of Certified Ledgerkeepers badge"></span>
    <span class="badge teal" role="img" aria-label="Continental League of Female Enterprise Founders badge"></span>
    <span class="badge shield" role="img" aria-label="LedgerPad certification badge"></span>
  </div>

  <div class="abs indicia">PRSRT STD<br>WCRWSS<br>U.S.POSTAGE<br>PAID<br>ZRPX RETAIL</div>

  <div class="abs brand-faint" aria-hidden="true">Bright Ledger<br>Accounting</div>

  <div class="abs contacts" style="left:40px;top:516px">
    <div class="row"><span class="ico"></span><span>555.318.2207</span><span class="sep">|</span><span class="ico"></span><span>1.800.555.0142</span></div>
    <div class="row"><span class="ico"></span><span>Info@<span class="hl">BrightLedgerAccounting</span>.com</span></div>
    <div class="row"><span class="ico"></span><span>www.<span class="hl">BrightLedgerAccounting</span>.com</span></div>
  </div>
</section>

</body>
</html>
```